We require a business card that promotes our Electrical business. Things we would like included are;
1) our business name, Bright Path Electrical and Communication
2) Our Electrical licence, EC 73620
3) Our ABN, 41 297 506 183
4) Our website, www.korvanelectric.com.au
5) Our Email, info@korvanelectric.com.au
6) Our contact number, 0462 158 704
7) Our address, 57 Larkfield Rd West Dunmore Perth 6109
8) Our logo, I will attach this (can you please change it so the ackground is white not black)
9) Our colours are red and white and perhaps some black
10) Managing Director Tomasz Relhuvan
11) the back to say 'notes' and have some lines for writing

Target Market(s)

General

Industry/Entity Type

Electrical

Contact Information for Business Card

Include the colour white, black and red.

Font styles to use
Sans Serif

Requirements
Nice to have
• A thunder bolt or a power point or a cord or something electrical, cartoon image of a cartoon like electrical tradie

```html
<!DOCTYPE html>
<html lang="en">
<head>
<meta charset="utf-8">
<title>Bright Path Electrical and Communication – Business Card</title>
<link rel="stylesheet" href="https://fonts.googleapis.com/css2?family=Open+Sans:wght@400;600;700&display=swap">
<style>
  :root {
    --red: #e8222f;
    --red-dark: #c91722;
    --white: #ffffff;
    --card: #f7f7f7;
    --ink: #2a2a2a;
    --line: #9a9a9a;
    --page: #e4e1dc;
  }
  * { margin: 0; padding: 0; box-sizing: border-box; }
  html, body {
    width: 1200px; height: 780px; overflow: hidden;
    background: var(--page);
    font-family: "Open Sans", Arial, sans-serif;
  }
  .stage { position: relative; width: 1200px; height: 780px; }

  .card {
    position: absolute;
    width: 540px; height: 310px;
    background: var(--card);
    box-shadow: 0 6px 18px rgba(0,0,0,0.18);
    overflow: hidden;
  }
  .card--front { left: 50px; top: 80px; }
  .card--back { left: 610px; top: 390px; }

  /* front */
  .corner-bar {
    position: absolute; right: 48px; top: 0;
    width: 56px; height: 12px; background: var(--red);
  }
  .business-name {
    position: absolute; left: 26px; top: 24px;
    color: var(--red); line-height: 1.05;
  }
  .business-name__main { font-size: 28px; font-weight: 700; display: block; }
  .business-name__sub { font-size: 20px; font-weight: 600; display: block; margin-top: 2px; }

  .name-band {
    position: absolute; left: 0; top: 108px;
    width: 290px; height: 48px;
    background: var(--red); color: var(--white);
    padding: 5px 0 0 26px;
  }
  .name-band__name { font-size: 20px; font-weight: 700; line-height: 1.1; display: block; }
  .name-band__title { font-size: 13px; font-weight: 400; display: block; }

  .contact {
    position: absolute; left: 26px; top: 168px;
    color: var(--ink); font-size: 13.5px; line-height: 1.35;
    list-style: none;
  }
  .contact li { display: flex; align-items: center; gap: 6px; }
  .contact .icon { width: 15px; height: 15px; flex: none; }
  .contact .abn-label { color: var(--red); }
  .website-front {
    position: absolute; left: 26px; bottom: 18px;
    color: var(--red); font-size: 13.5px;
  }

  .brand-mark {
    position: absolute; left: 330px; top: 108px;
    display: flex; align-items: center; gap: 10px;
    color: var(--red); font-size: 22px; font-weight: 700;
  }
  .brand-mark__dot {
    width: 26px; height: 26px; border-radius: 50%; background: var(--red);
  }
  .licence {
    position: absolute; right: 26px; top: 26px;
    text-align: right; color: var(--ink); font-size: 13.5px; line-height: 1.25;
  }

  /* back */
  .back-title {
    position: absolute; left: 0; right: 0; top: 30px;
    text-align: center; color: var(--red); line-height: 1.1;
  }
  .back-title__main { font-size: 26px; font-weight: 600; display: block; }
  .back-title__sub { font-size: 18px; font-weight: 400; display: block; }
  .notes-label {
    position: absolute; left: 0; right: 0; top: 118px;
    text-align: center; color: var(--red); font-size: 22px; font-weight: 400;
  }
  .note-lines { position: absolute; left: 40px; right: 40px; top: 170px; }
  .note-lines span {
    display: block; height: 1px; background: var(--line); margin-bottom: 30px;
  }
  .website-back {
    position: absolute; left: 0; right: 0; bottom: 18px;
    text-align: center; color: var(--red); font-size: 13px;
  }
</style>
</head>
<body>
<main class="stage">

  <section class="card card--front" aria-label="Business card front">
    <div class="corner-bar"></div>
    <h1 class="business-name">
      <span class="business-name__main">Bright Path Electrical</span>
      <span class="business-name__sub">and Communication</span>
    </h1>

    <div class="name-band">
      <span class="name-band__name">Tomasz Relhuvan</span>
      <span class="name-band__title">Managing Director</span>
    </div>

    <ul class="contact">
      <li>57 Larkfield Rd</li>
      <li>West Dunmore Perth 6109</li>
      <li>
        <svg class="icon" viewBox="0 0 15 15" aria-hidden="true">
          <rect width="15" height="15" rx="2" fill="#e8222f"/>
          <path d="M4 3.5h2l.8 2-1.2.9a5 5 0 0 0 3 3l.9-1.2 2 .8v2a1 1 0 0 1-1 1A7.5 7.5 0 0 1 3 4.5a1 1 0 0 1 1-1z" fill="#fff"/>
        </svg>
        0462 158 704
      </li>
      <li>
        <svg class="icon" viewBox="0 0 15 15" aria-hidden="true">
          <rect width="15" height="15" rx="2" fill="#e8222f"/>
          <rect x="3" y="4.5" width="9" height="6" fill="none" stroke="#fff" stroke-width="1.1"/>
          <path d="M3 4.5l4.5 3.5 4.5-3.5" fill="none" stroke="#fff" stroke-width="1.1"/>
        </svg>
        info@korvanelectric.com.au
      </li>
      <li><span class="abn-label">ABN</span> 41 297 506 183</li>
    </ul>
    <p class="website-front">www.korvanelectric.com.au</p>

    <div class="brand-mark">
      <span class="brand-mark__dot"></span>
      <span>Bright Path</span>
    </div>

    <p class="licence">Electrical licence<br>EC 73620</p>
  </section>

  <section class="card card--back" aria-label="Business card back">
    <h2 class="back-title">
      <span class="back-title__main">Bright Path Electrical</span>
      <span class="back-title__sub">and Communication</span>
    </h2>
    <p class="notes-label">Notes</p>
    <div class="note-lines"><span></span><span></span><span></span></div>
    <p class="website-back">www.korvanelectric.com.au</p>
  </section>

</main>
</body>
</html>
```